Volmira Logo and business card

We need a business card and logo, we are currently using a logo that we like but would like to be a bit more streamlined. We deal with very high end clients and our business card needs to reflect that. We would love to see and hire somebody that can deliver a very MODERN, simple design. With he main front of the card to be black with either a red lettering or White to provide great contrast. I would like to have a minimalist abstract picture of a heavy machine on it but it is not a requirement ( most likely an Crane ( a bold heron crane with a bucket would be perfect or maybe a vendari 270 XT )) If it keeps in line with being a classic simple, and modern design. Letterpress is also an option where it gives it a great look and texture, the card will be printed on a thick stock. On the back there needs to be a star included somewhere on the card and design, this represents the first generation that started the company back in 1936 therefore it is a sentimental addition ( make it modern and simple)
We do not want a cheesy construction template. We do heavy site work, aka we use excavators, payloaders, off road rok j40 trucks, very big fun toys.
There is a huge chance to get the web design as well for the winning design.
Have fun, cannot wait to see the designs!
In addition, we'd like to point out that our primary need and priority is still the BUSINESS CARD design itself. The logo has to complement the overall look of the business card, but it is secondary to the card's look. Please keep this in mind.
Thank you,
Gerald
Target Market(s)
General Contractors, upscale home owners ( house values of 1M plus)
and commercial property owners.
Projects range from $5000 to 1 million.
Industry/Entity Type
Construction
Requirements
Must have
- Star incorporated into design
Nice to have
- an abstract heavy site work machine ( pics attached) If it keeps in line with being a classic simple, and modern design.
I would like to have black and red on the design since all the lettering on the trucks is red, but i will let the designer take care of that.

```html
<!DOCTYPE html>
<html lang="en">
<head>
<meta charset="utf-8">
<title>Volmira Industries Inc. – Business Card</title>
<link href="https://fonts.googleapis.com/css2?family=Michroma&family=Orbitron:wght@700;800&display=swap" rel="stylesheet">
<style>
  :root {
    --stage: #1b1b1b;
    --card-white: #f4f4f4;
    --card-black: #1f1f1f;
    --card-band: #141414;
    --red: #e0161b;
    --grey: #5e5e5e;
    --white: #ffffff;
  }
  * { margin: 0; padding: 0; box-sizing: border-box; }
  html, body {
    width: 1200px; height: 849px; overflow: hidden;
    background: var(--stage);
    font-family: "Michroma", sans-serif;
  }
  .canvas { position: relative; width: 1200px; height: 849px; }

  .card {
    position: absolute; width: 490px; height: 280px;
    top: 170px; box-shadow: 0 14px 30px rgba(0,0,0,.55);
  }
  .card--front {
    left: 80px; background: var(--card-white);
    display: flex; align-items: center; justify-content: center;
  }
  .card--back { left: 630px; background: var(--card-black); overflow: hidden; }

  .wordmark {
    display: flex; flex-direction: column; align-items: flex-start; gap: 3px;
    font-family: "Orbitron", sans-serif; font-weight: 800; color: var(--red);
  }
  .wordmark__row { display: flex; align-items: center; gap: 8px; }
  .wordmark__square { width: 12px; height: 12px; background: var(--red); }
  .wordmark__name { letter-spacing: .03em; line-height: 1; }
  .wordmark__sub { letter-spacing: .06em; line-height: 1; }

  .card--front .wordmark__name { font-size: 32px; }
  .card--front .wordmark__sub { font-size: 11px; padding-left: 20px; }

  .card--back .wordmark { position: absolute; left: 26px; top: 34px; }
  .card--back .wordmark__name { font-size: 18px; }
  .card--back .wordmark__sub { font-size: 7px; padding-left: 16px; }
  .card--back .wordmark__square { width: 8px; height: 8px; }

  .person { position: absolute; right: 26px; top: 118px; text-align: right; }
  .person__name {
    color: var(--red); font-family: "Orbitron", sans-serif; font-weight: 800;
    font-size: 17px; letter-spacing: .06em;
  }
  .person__title { color: var(--grey); font-size: 10px; letter-spacing: .1em; margin-top: 6px; }

  .contact {
    position: absolute; right: 26px; top: 172px; text-align: right;
    color: var(--grey); font-size: 9.5px; letter-spacing: .05em; line-height: 2;
  }
  .card__band {
    position: absolute; left: 0; right: 0; bottom: 0; height: 58px;
    background: var(--card-band);
  }

  .brand-lockup {
    position: absolute; right: 38px; bottom: 36px;
    display: flex; flex-direction: column; align-items: center; gap: 6px;
    font-family: "Orbitron", sans-serif; font-weight: 800; color: var(--white);
  }
  .brand-lockup .wordmark__square { background: var(--white); width: 18px; height: 18px; margin-bottom: 10px; }
  .brand-lockup__name { font-size: 34px; letter-spacing: .04em; line-height: 1; }
  .brand-lockup__sub { font-size: 13px; letter-spacing: .06em; }
</style>
</head>
<body>
<main class="canvas">
  <section class="card card--front" aria-label="Card front">
    <div class="wordmark">
      <div class="wordmark__row">
        <span class="wordmark__square"></span>
        <span class="wordmark__name">VOLMIRA</span>
      </div>
      <span class="wordmark__sub">INDUSTRIES INC.</span>
    </div>
  </section>

  <section class="card card--back" aria-label="Card back">
    <div class="card__band"></div>
    <div class="wordmark">
      <div class="wordmark__row">
        <span class="wordmark__square"></span>
        <span class="wordmark__name">VOLMIRA</span>
      </div>
      <span class="wordmark__sub">INDUSTRIES INC.</span>
    </div>
    <div class="person">
      <p class="person__name">NAME SURNAME</p>
      <p class="person__title">TITLE</p>
    </div>
    <div class="contact">
      <p>PHONE: 0000 0000 000 &nbsp;E-MAIL: AAAAAA@VOLMIRA.COM</p>
      <p>WWW.VOLMIRA.COM</p>
    </div>
  </section>

  <div class="brand-lockup">
    <span class="wordmark__square"></span>
    <span class="brand-lockup__name">VOLMIRA</span>
    <span class="brand-lockup__sub">INDUSTRIES INC.</span>
  </div>
</main>
</body>
</html>
```